Sticker Design

Wanting business name across the bottom of car doors, please see attached. looking for something simple and require asap. Happy for black and white simple colouring.

Thank you
Dane Morvill

```html
<!DOCTYPE html>
<html lang="en">
<head>
<meta charset="utf-8">
<title>MVR Field Service and Logistics – Door Sticker</title>
<link href="https://fonts.googleapis.com/css2?family=Michroma&display=swap" rel="stylesheet">
<style>
  :root {
    --backdrop: #e6e6e6;
    --band: #000000;
    --ink: #ffffff;
  }
  html, body {
    margin: 0;
    padding: 0;
    width: 1200px;
    height: 251px;
    overflow: hidden;
    background: var(--backdrop);
  }
  .canvas {
    position: relative;
    width: 1200px;
    height: 251px;
  }
  .door-band {
    position: absolute;
    left: 69px;
    top: 82px;
    width: 1068px;
    height: 88px;
    background: var(--band);
    overflow: hidden;
    color: var(--ink);
    font-family: "Michroma", sans-serif;
  }
  .brand {
    position: absolute;
    left: 58px;
    top: 14px;
    height: 60px;
    display: flex;
    align-items: center;
    gap: 8px;
  }
  .brand-name {
    font-size: 36px;
    line-height: 1;
    letter-spacing: 2px;
  }
  .brand-dot {
    width: 34px;
    height: 34px;
    border: 4px solid var(--ink);
    border-radius: 50%;
    box-sizing: border-box;
  }
  .tagline {
    position: absolute;
    left: 234px;
    top: 24px;
    margin: 0;
    font-size: 20px;
    line-height: 22px;
    letter-spacing: 4.4px;
    font-weight: 400;
    white-space: nowrap;
  }
  .tagline span { display: block; }
  .divider {
    position: absolute;
    left: 569px;
    top: 16px;
    width: 4px;
    height: 60px;
    background: var(--ink);
  }
  .phone {
    position: absolute;
    left: 605px;
    top: 27px;
    font-size: 30px;
    line-height: 34px;
    letter-spacing: 6px;
    white-space: nowrap;
  }
</style>
</head>
<body>
<div class="canvas">
  <div class="door-band">
    <div class="brand">
      <span class="brand-name">MVR</span>
      <span class="brand-dot" aria-hidden="true"></span>
    </div>
    <h1 class="tagline"><span>FIELD SERVICE</span><span>AND LOGISTICS</span></h1>
    <div class="divider" aria-hidden="true"></div>
    <div class="phone">0412570386</div>
  </div>
</div>
</body>
</html>
```